Web Design Project

Please design a new website template for Larkspurleigh as follows -

Existing Website - http://www.larkspurleigh.com.au/

Logo - http://brightquaydesk.com/Design/larkspurleigh-logo

Navigation - Top Horizontal

Colours: Pink and purple from attached logo (do not use the bright pink from the existing website)

Page Structure: Home, About Us, Services, The Team, Key Contacts, Our Values, Send Resume, Timesheets, Candidates, Clients, Location, Contact Us.

The template should include an enquiry from on all pages with fields: Name, Phone, Email, Enquiry

The template should include their phone number in the top right corner - (08) 9617 2259

It should include a tag line: Temporary & Permanent Support Staff Specialists

The Footer:
Level 5, 7 Tembley Parade
SUBIACO
WA 6008
Phone - (08) 9617 2259
Fax - (08) 9617 2271
Email - admin@larkspurleigh.com.au

Websites they like - http://www.dwightmorrowcosmeticclinic.com.au/ (preferably keep the text on a white background on this site)

Include a button/icon for - Job Listings

Home page text - Use what is on their existing website (you can reduce the number of bullet points)

Reason: I will review this job tomorrow and make a decision then, please upload psd files for all projects.

Reason: We have made a decisions, just waiting on some updates from your end.

Reason: I need the psd file please.

```html
<!DOCTYPE html>
<html lang="en">
<head>
<meta charset="utf-8">
<title>Larkspurleigh - The Recruitment Bureau</title>
<link rel="stylesheet" href="https://fonts.googleapis.com/css2?family=Noto+Serif:wght@400;700&display=swap">
<style>
  :root {
    --pink: #e54d9b;
    --pink-dark: #d23c88;
    --purple: #5a2a85;
    --heading-purple: #5b2d8a;
    --text: #2b2b2b;
    --panel: #f4f4f4;
    --line: #d9d9d9;
    --white: #ffffff;
  }
  * { box-sizing: border-box; margin: 0; padding: 0; }
  html, body { width: 1200px; height: 1078px; overflow: hidden; }
  body { font-family: "Noto Serif", Georgia, serif; color: var(--text); background: var(--white); position: relative; }
  .wrap { width: 856px; margin: 0 auto; position: relative; }

  .site-header { background: var(--pink); height: 142px; }
  .site-header .wrap { height: 142px; }
  .brand { position: absolute; left: 0; top: 52px; display: flex; align-items: center; gap: 12px; }
  .brand-dot { width: 30px; height: 30px; border-radius: 50%; background: var(--purple); }
  .brand-name { font-size: 34px; color: #2a1236; font-weight: 400; letter-spacing: 1px; }
  .header-call { position: absolute; right: 0; top: 50px; text-align: right; color: var(--white); white-space: nowrap; }
  .header-call .phone { font-size: 35px; line-height: 1; letter-spacing: 0.5px; }
  .header-call .tagline { font-size: 12.5px; margin-top: 6px; }

  .main-nav { background: linear-gradient(#7544a2, #5e2f8a); height: 36px; border-bottom: 2px solid #c9c9c9; }
  .nav-list { list-style: none; display: flex; height: 34px; align-items: center; white-space: nowrap; }
  .nav-list li { font-size: 12.5px; color: var(--white); padding: 0 6.3px; border-left: 1px dotted rgba(255,255,255,0.55); line-height: 16px; white-space: nowrap; }
  .nav-list li:first-child { border-left: none; padding-left: 1px; }

  .hero-band { background: var(--panel); height: 305px; border-bottom: 1px solid #e2e2e2; padding-top: 16px; }
  .hero { height: 276px; background: var(--white); border-radius: 4px; position: relative; overflow: hidden; }
  .hero-photo { position: absolute; left: 170px; right: 0; top: 0; bottom: 0;
    background: radial-gradient(ellipse at 70% 80%, #3b3b44 0%, #7a6a66 30%, #e8dcd6 60%, #ffffff 85%); opacity: 0.85; }
  .hero-title { position: absolute; left: 10px; top: 2px; font-size: 44px; font-weight: 400; color: #252525; white-space: nowrap; }
  .hero-sub { position: absolute; left: 11px; top: 64px; font-size: 22px; line-height: 29px; color: var(--pink); font-weight: 400; white-space: nowrap; }

  .content { padding-top: 14px; height: 449px; }
  .intro { width: 565px; }
  .intro h1 { font-size: 22px; font-weight: 400; color: var(--heading-purple); white-space: nowrap; }
  .intro h2 { font-size: 16px; font-weight: 400; color: var(--pink); margin-top: 14px; white-space: nowrap; }
  .intro p { font-size: 12.5px; line-height: 19px; margin-top: 12px; }
  .areas { display: flex; margin-top: 12px; }
  .areas ul { list-style: none; width: 277px; }
  .areas li { font-size: 12.5px; line-height: 19.2px; white-space: nowrap; }
  .areas li::before { content: "»"; color: var(--pink); margin-right: 7px; font-size: 11px; }

  .enquiry { position: absolute; right: 0; top: 18px; width: 276px; height: 367px; background: var(--panel); border-radius: 3px; box-shadow: 0 2px 3px rgba(0,0,0,0.15); }
  .enquiry-head { background: linear-gradient(#8a55bb, #6a3598); color: var(--white); padding: 5px 7px 6px; border-radius: 3px 3px 0 0; height: 62px; }
  .enquiry-head h3 { font-size: 16px; font-weight: 400; line-height: 20px; }
  .enquiry-head p { font-size: 10.5px; line-height: 16px; margin-top: 2px; }
  .field { display: flex; align-items: center; margin: 9px 8px 0 9px; height: 23px; font-size: 12.5px; }
  .field:first-of-type { margin-top: 11px; }
  .field label { width: 61px; }
  .field span.input { flex: 1; height: 23px; background: var(--white); border: 1px solid var(--line); }
  .enquiry-label { font-size: 12.5px; margin: 10px 0 0 9px; }
  .enquiry-box { margin: 8px 9px 0 7px; height: 88px; background: var(--white); border: 1px solid var(--line); }
  .callback { display: block; margin: 21px 0 0 49px; width: 197px; height: 39px; border-radius: 3px; background: linear-gradient(#ee6cae, #e24797); border: 1px solid var(--pink-dark); color: var(--white); font-family: inherit; font-size: 16px; white-space: nowrap; }

  .site-footer { background: linear-gradient(#4b2375, #553086); height: 146px; color: var(--white); }
  .site-footer .wrap { height: 146px; }
  .footer-links { padding-top: 20px; }
  .footer-row { list-style: none; display: flex; white-space: nowrap; margin-bottom: 6px; }
  .footer-row li { font-size: 12.5px; padding: 0 6.3px; border-right: 1px dotted rgba(255,255,255,0.55); line-height: 16px; white-space: nowrap; }
  .footer-row li:first-child { padding-left: 1px; }
  .footer-row li.last { border-right: none; }
  .copyright { position: absolute; left: 0; top: 111px; font-size: 10.5px; white-space: nowrap; }
  .footer-address { position: absolute; left: 627px; top: 18px; font-size: 12.5px; line-height: 18.7px; font-style: normal; white-space: nowrap; }
</style>
</head>
<body>
  <header class="site-header">
    <div class="wrap">
      <div class="brand"><span class="brand-dot"></span><span class="brand-name">LARKSPURLEIGH</span></div>
      <div class="header-call">
        <div class="phone">CALL 08 9617 2259</div>
        <div class="tagline">Temporary &amp; Permanent Support Staff Specialists</div>
      </div>
    </div>
  </header>

  <nav class="main-nav">
    <div class="wrap">
      <ul class="nav-list">
        <li>Home</li><li>About Us</li><li>Services</li><li>The Team</li><li>Key Contacts</li><li>Our Values</li><li>Send Resume</li><li>Timesheets</li><li>Candidates</li><li>Clients</li><li>Location</li><li>Contact Us</li>
      </ul>
    </div>
  </nav>

  <section class="hero-band">
    <div class="wrap hero">
      <div class="hero-photo" role="img" aria-label="Photo of four smiling young office professionals in business attire"></div>
      <h2 class="hero-title">Looking for a Job?</h2>
      <p class="hero-sub">Let our experienced team service you to finding<br>that temporary or permanent job!</p>
    </div>
  </section>

  <main class="wrap content">
    <section class="intro">
      <h1>Larkspurleigh - The Recruitment Bureau</h1>
      <h2>"Support Staff Specialists - Temporary and Permanent"</h2>
      <p>Larkspurleigh has impeccable credentials. Our experienced and thoroughly professional team services a broad range of blue-chip national and multi-national companies with the recruit-ment of temporary and permanent staff in the areas of:</p>
      <div class="areas">
        <ul>
          <li>Administration</li><li>Personal Assistant</li><li>Executive Assistant</li><li>Reception</li><li>Legal</li><li>Secretaries</li><li>Accounts Clerk</li>
        </ul>
        <ul>
          <li>Project Engineering</li><li>Construction and Property</li><li>Accounting</li><li>Customer Service</li><li>Data Entry</li><li>Cell Centre</li><li>Project Engineering</li>
        </ul>
      </div>
    </section>

    <aside class="enquiry">
      <div class="enquiry-head">
        <h3>FIND OUT MORE</h3>
        <p>Complete this form and we'll get back to you within 24 hours to answer your questions!</p>
      </div>
      <div class="field"><label>Name*:</label><span class="input"></span></div>
      <div class="field"><label>Phone:</label><span class="input"></span></div>
      <div class="field"><label>E-mail:</label><span class="input"></span></div>
      <div class="enquiry-label">Enquiry:</div>
      <div class="enquiry-box"></div>
      <button class="callback" type="button">Request A Call Back</button>
    </aside>
  </main>

  <footer class="site-footer">
    <div class="wrap">
      <div class="footer-links">
        <ul class="footer-row">
          <li>Home</li><li>About Us</li><li>Services</li><li>The Team</li><li>Key Contacts</li><li>Our Values</li><li>Send Resume</li>
        </ul>
        <ul class="footer-row">
          <li>Timesheets</li><li>Candidates</li><li>Clients</li><li>Location</li><li class="last">Contact Us</li>
        </ul>
      </div>
      <div class="copyright">Copyright © 2012 Larkspurleigh. All Rights Reserved.</div>
      <address class="footer-address">
        Level 5, 7 Tembley Parade<br>SUBIACO<br>WA 6008<br>Phone - (08) 9617 2259<br>Fax - (08) 9617 2271<br>Email - admin@larkspurleigh.com.au
      </address>
    </div>
  </footer>
</body>
</html>
```